Book Cover for my Autobiography

I would like to see a CONCEPT of the Front Cover as per the following.
a) Take me out of the FILE NAMED=1-MAIN.jpg
b) I want my Wife "Watching over me" - behind me - in the SHADOWS. You can take her image for the concept from the FILE NAMED=2-Wife Watching over me.jpg.
c) This based on the old saying that "Behind every Good Man....is a Woman".  So that's what I want to convert because my wife has always been in the background, in the "Shadows" - always supporting and encouraging me in whatever I do.
d) This book is purely for my children, wife, siblings, relatives and Friends.
e) the Book Cover has to be designed FLAT & RECTANGULAR - like the sample leather cover.  i.e. NOT viewed from an Angle.
f) The Book Title is "Paper Boats Home"
g) I have no pre-conceived ideas of design or colours or styling etc.  I want a PROFESSIONAL DESIGNER to come up with the best Overall Design that conveys the "Supportive Wife" always behind me and supporting me - While I am out front as the subject.
h) When the Design is accepted, I will provide the main photo of my wife without my son in front of her that I want to use - and one me without my wife's arms around me.  But if you can do that too (i.e. reconstruct my Wife's Burgundy top & and remove her arms from around me-then even better because I don't have to hire another graphic designer to do that for me).
My name is "Rupert ten Brakel" so the author of the autobiography needs to be SOMEWHERE.
h) And last, please just put some text - maybe 2 sentences for the summary of the story like many Autobiographies do. eg.
"My story of how ....Lorem ipsum dolor sit amet, consectetur adipiscing elit, sed do eiusmod tempor incididunt. Integer vitae justo eget magna fermentum iaculis eu non. Aliquam eleifend".

I forgot to mention that this Book Cover is actually going on an eBOOK - not a Printed Book.
It's just for Family and Friends.

```html
<!DOCTYPE html>
<html lang="en">
<head>
<meta charset="utf-8">
<title>Paper Boats Home — Rupert ten Brakel</title>
<link rel="stylesheet" href="https://fonts.googleapis.com/css2?family=Great+Vibes&family=Open+Sans:wght@400&display=swap">
<style>
  :root {
    --page-bg: #b9eefb;
    --cover-blue: #0d8fe8;
    --cover-edge: #0a82d6;
    --supporter-hair: #1a4f86;
    --supporter-skin: #3f7ab4;
    --supporter-top: #4a5a98;
    --author-hair: #1c1f2c;
    --author-skin: #9a7466;
    --author-beard: #3a2a28;
    --author-collar: #b5344a;
    --author-sweater: #232f86;
    --author-sweater-light: #2a3a98;
    --text-light: #ffffff;
  }
  * { margin: 0; padding: 0; box-sizing: border-box; }
  html, body {
    width: 1200px;
    height: 1200px;
    overflow: hidden;
    background: var(--page-bg);
  }
  .canvas {
    position: relative;
    width: 1200px;
    height: 1200px;
  }
  .cover {
    position: absolute;
    left: 186px;
    top: 0;
    width: 828px;
    height: 1200px;
    background: var(--cover-blue);
    overflow: hidden;
    box-shadow: inset 6px 0 0 var(--cover-edge);
  }
  .portrait-supporter {
    position: absolute;
    left: 48px;
    top: 221px;
    width: 416px;
    height: 524px;
    border-radius: 48% 48% 22% 22% / 58% 58% 14% 14%;
    background: linear-gradient(to bottom,
      var(--supporter-hair) 0%,
      var(--supporter-hair) 14%,
      var(--supporter-skin) 26%,
      var(--supporter-skin) 46%,
      var(--supporter-hair) 56%,
      var(--supporter-top) 68%,
      var(--cover-blue) 92%);
    -webkit-mask-image: linear-gradient(to bottom, #000 60%, transparent 92%);
    mask-image: linear-gradient(to bottom, #000 60%, transparent 92%);
    opacity: 0.8;
  }
  .portrait-author {
    position: absolute;
    left: 325px;
    top: 516px;
    width: 503px;
    height: 684px;
    border-radius: 60% 40% 0 0 / 32% 22% 0 0;
    background: linear-gradient(to bottom,
      var(--author-hair) 0%,
      var(--author-hair) 16%,
      var(--author-skin) 26%,
      var(--author-skin) 38%,
      var(--author-beard) 46%,
      var(--author-beard) 52%,
      var(--author-collar) 57%,
      var(--author-collar) 62%,
      var(--author-sweater-light) 67%,
      var(--author-sweater) 100%);
  }
  .title {
    position: absolute;
    inset: 0;
    font-family: "Great Vibes", cursive;
    font-weight: 400;
    color: var(--text-light);
    text-shadow: 0 2px 3px rgba(0, 40, 90, 0.45);
    pointer-events: none;
  }
  .title-line {
    position: absolute;
    font-size: 104px;
    line-height: 1;
    white-space: nowrap;
  }
  .title-line--first { left: 474px; top: 70px; }
  .title-line--second { left: 340px; top: 132px; }
  .title-line--third { left: 494px; top: 210px; }
  .author {
    position: absolute;
    left: 536px;
    top: 390px;
    font-family: "Open Sans", sans-serif;
    font-size: 26px;
    font-weight: 400;
    color: var(--text-light);
    white-space: nowrap;
  }
  .summary {
    position: absolute;
    left: 59px;
    top: 1036px;
    width: 640px;
    font-family: "Open Sans", sans-serif;
    font-size: 16.5px;
    line-height: 33px;
    color: var(--text-light);
  }
  .summary span { display: block; white-space: nowrap; }
</style>
</head>
<body>
  <main class="canvas">
    <section class="cover">
      <div class="portrait-supporter" role="img" aria-label="Soft, faded portrait of the author's wife with dark shoulder-length hair and a burgundy top, smiling and watching over him from the background"></div>
      <div class="portrait-author" role="img" aria-label="Portrait of the bearded author smiling, wearing a navy sweater over a red checked shirt, arms folded"></div>

      <h1 class="title" aria-label="Paper Boats Home">
        <span class="title-line title-line--first">Paper</span>
        <span class="title-line title-line--second">Boats</span>
        <span class="title-line title-line--third">Home</span>
      </h1>

      <p class="author">Rupert ten Brakel</p>

      <p class="summary">
        <span>"My story of how ....Lorem ipsum dolor sit amet,</span>
        <span>consectetur adipiscing elit, sed do eiusmod tempor incididunt.</span>
        <span>Integer vitae justo eget magna fermentum iaculis eu non. Aliquam eleifend".</span>
      </p>
    </section>
  </main>
</body>
</html>
```